New Modern floristry business design

Hi, we are a new business based in Sydney called "copper fern floristry"

With so many floristry's we need a good design that will set a great first impression.

A few descriptive words on how we envision copper fern floristry:

-dynamic design
-minimal colour (colour can be used to enhance the design)
-black white grey (can include gold,silver,metallic shadowing)
Strong "COPPER FERN" with a classy "FLORISTRY"
Bold with a touch of feminine

Copper Fern Floristry,
Delia Varnet,
Copperfernfloristry@mailbay.com.au

```html
<!DOCTYPE html>
<html lang="en">
<head>
<meta charset="utf-8">
<title>Copper Fern Floristry – Business Cards</title>
<link rel="stylesheet" href="https://fonts.googleapis.com/css2?family=Quicksand:wght@400;600&family=Kaushan+Script&display=swap">
<style>
  :root {
    --page: #ffffff;
    --card-charcoal: #333333;
    --card-black: #1a1a1b;
    --gold: #d9cb3c;
    --name-gold: #ece24f;
    --muted-grey: #8c8c8c;
    --icon-grey: #6e6e6e;
    --white: #ffffff;
  }
  * { margin: 0; padding: 0; box-sizing: border-box; }
  html, body {
    width: 1200px; height: 800px; overflow: hidden;
    background: var(--page);
  }
  .sheet { position: relative; width: 1200px; height: 800px; }
  .card {
    position: absolute; width: 476px; height: 280px;
    display: flex; flex-direction: column; align-items: center;
  }
  .card--charcoal { background: var(--card-charcoal); }
  .card--black { background: var(--card-black); }
  .card--back-top { left: 90px; top: 74px; }
  .card--front-top { left: 634px; top: 74px; }
  .card--back-bottom { left: 90px; top: 445px; }
  .card--front-bottom { left: 634px; top: 445px; }

  .contact { padding-top: 96px; }
  .contact__icon { width: 54px; height: 54px; display: block; }
  .contact__email {
    margin-top: 4px;
    font-family: "Quicksand", sans-serif; font-weight: 400;
    font-size: 21px; letter-spacing: 0.2px;
  }
  .card--charcoal .contact__email { color: var(--muted-grey); }
  .card--black .contact__email { color: var(--white); }

  .brand {
    position: absolute; left: 104px; top: 62px;
    display: flex; align-items: center; gap: 12px;
  }
  .brand__dot { width: 44px; height: 44px; border-radius: 50%; }
  .brand__name {
    font-family: "Quicksand", sans-serif; font-weight: 600;
    font-size: 27px; margin-top: 46px; white-space: nowrap;
  }
  .holder {
    position: absolute; left: 0; right: 0; top: 196px; text-align: center;
    font-family: "Kaushan Script", cursive; font-size: 22px;
  }
  .card--charcoal .brand__dot { background: var(--gold); }
  .card--charcoal .brand__name { color: var(--gold); }
  .card--charcoal .holder { color: var(--name-gold); }
  .card--black .brand__dot { background: var(--white); }
  .card--black .brand__name { color: var(--white); }
  .card--black .holder { color: var(--white); }
</style>
</head>
<body>
<main class="sheet">
  <section class="card card--charcoal card--back-top">
    <div class="contact">
      <svg class="contact__icon" viewBox="0 0 54 54" aria-hidden="true">
        <circle cx="27" cy="27" r="25" fill="var(--icon-grey)"/>
        <rect x="14" y="18" width="26" height="18" fill="var(--card-charcoal)"/>
        <path d="M14 18 L27 29 L40 18" fill="none" stroke="var(--icon-grey)" stroke-width="2"/>
      </svg>
    </div>
    <p class="contact__email">Copperfernfloristry@mailbay.com.au</p>
  </section>

  <section class="card card--charcoal card--front-top">
    <div class="brand">
      <span class="brand__dot"></span>
      <span class="brand__name">Copper Fern Floristry</span>
    </div>
    <p class="holder">Delia Varnet</p>
  </section>

  <section class="card card--black card--back-bottom">
    <div class="contact">
      <svg class="contact__icon" viewBox="0 0 54 54" aria-hidden="true">
        <circle cx="27" cy="27" r="25" fill="var(--white)"/>
        <rect x="14" y="18" width="26" height="18" fill="var(--card-black)"/>
        <path d="M14 18 L27 29 L40 18" fill="none" stroke="var(--white)" stroke-width="2"/>
      </svg>
    </div>
    <p class="contact__email">Copperfernfloristry@mailbay.com.au</p>
  </section>

  <section class="card card--black card--front-bottom">
    <div class="brand">
      <span class="brand__dot"></span>
      <span class="brand__name">Copper Fern Floristry</span>
    </div>
    <p class="holder">Delia Varnet</p>
  </section>
</main>
</body>
</html>
```